Wine Bottle Label Graphic Design (mini bottle 187ml)

Looking for a contemporary custom wine label design for party favors. Inspiration photos provided. **Please see "wine favorite" example in uploads.

Artwork 2.5" wide by 2.75" tall to be placed on 3"x3" stickers. Specs from printer attached but I still want image to fit within the artwork size I specified. Please make label center justified. This is for BOYS. It does not need to be super "masculine"...but definitely not feminine.

Required elements:

Colors: white background, include gold and purple to match logo. Other colors are fine to include.

Name: Sababa 13 (I like use of the No) as shown in the sample, but not required
Varietal: Mitzvah Blend 6.11.2021
Vineyard: Hollis Family Vineyard
Location: Maryland
Logo: See attached (KRNotecard Final)

Font styles to use
Serif
Sans Serif

Requirements
Must have
• All the above elements. Clean and crisp design. Contemporary and classy. Purple, Gold, Black colors. See logo. You CAN include cursive font for select elements. I don't mind a combination of print and script.
Should not have
• Floral, scrolling, background image, old fashioned

```html
<!DOCTYPE html>
<html lang="en">
<head>
<meta charset="utf-8">
<title>Sababa 13 – Mitzvah Blend Label</title>
<link rel="stylesheet" href="https://fonts.googleapis.com/css2?family=Jost:wght@300;400&family=Pinyon+Script&display=swap">
<style>
  :root {
    --canvas: #f2f2f4;
    --label-bg: #ffffff;
    --label-edge: #6b6b6b;
    --purple: #431651;
    --gold: #c9a44c;
  }
  * { margin: 0; padding: 0; box-sizing: border-box; }
  html, body {
    width: 1200px;
    height: 1000px;
    overflow: hidden;
    background: var(--canvas);
  }
  .label {
    position: absolute;
    left: 330px;
    top: 203px;
    width: 540px;
    height: 594px;
    background: var(--label-bg);
    border: 1px solid var(--label-edge);
    color: var(--purple);
    font-family: "Jost", sans-serif;
  }
  .wine-name__word {
    position: absolute;
    left: 156px;
    top: 60px;
    height: 190px;
    writing-mode: vertical-rl;
    font-weight: 300;
    font-size: 38px;
    line-height: 1;
    letter-spacing: 0.16em;
    text-transform: uppercase;
  }
  .wine-name__number {
    position: absolute;
    left: 200px;
    top: 24px;
    font-weight: 400;
    font-size: 268px;
    line-height: 1;
    letter-spacing: 0.02em;
  }
  .varietal {
    position: absolute;
    left: 0;
    top: 258px;
    width: 100%;
    text-align: center;
    font-size: 26px;
    font-weight: 400;
    letter-spacing: 0.03em;
  }
  .family-mark {
    position: absolute;
    left: 0;
    top: 375px;
    width: 100%;
    display: flex;
    align-items: center;
    justify-content: center;
    gap: 12px;
  }
  .family-mark__dot {
    width: 30px;
    height: 30px;
    border-radius: 50%;
    background: var(--gold);
  }
  .family-mark__name {
    font-size: 28px;
    font-weight: 400;
    letter-spacing: 0.08em;
    text-transform: uppercase;
  }
  .vineyard {
    position: absolute;
    left: 0;
    top: 490px;
    width: 100%;
    text-align: center;
    font-size: 27px;
    font-weight: 400;
    letter-spacing: 0.03em;
  }
  .location {
    position: absolute;
    left: 0;
    top: 520px;
    width: 100%;
    text-align: center;
    font-family: "Pinyon Script", cursive;
    font-size: 40px;
    line-height: 1.1;
  }
</style>
</head>
<body>
  <main class="label">
    <h1 class="wine-name" aria-label="Sababa 13">
      <span class="wine-name__word">Sababa</span>
      <span class="wine-name__number">13</span>
    </h1>
    <p class="varietal">Mitzvah Blend 2021</p>
    <div class="family-mark">
      <span class="family-mark__dot"></span>
      <span class="family-mark__name">Kevin &amp; Reid</span>
    </div>
    <p class="vineyard">Hollis Family Vineyard</p>
    <p class="location">Maryland</p>
  </main>
</body>
</html>
```